Driver License Monitoring Application Marketing Website

We need a new web design for our web application. The product is called "PermitPulse." We provide a driver license monitoring service to companies and local government bodies with driver fleets. Our current website is available at www.permitpulse-example.com.

I prefer a clean, single-page design with good SEO. Attached are some PDFs with data about the project.

Target Market(s)

Companies with driver fleets, local government.

Industry/Entity Type

Government

Coding

Coded - Design and coding required

Number of Pages Required

1 page

Colors
000000

Requirements
Must have
• Content from current www.permitpulse-example.com and attached PDFs.
Nice to have
• Prefer a simple Bootstrap or similar design for easy editing.
• Room for a simple video explanation of how the product works (we don't have an actual video yet)

```html
<!DOCTYPE html>
<html lang="en">
<head>
<meta charset="utf-8">
<title>PermitPulse – Florida Driver License Monitoring</title>
<link rel="stylesheet" href="https://fonts.googleapis.com/css2?family=Cinzel:wght@400;700&family=Open+Sans:wght@400;600&display=swap">
<style>
  :root {
    --red: #b3222a;
    --red-dark: #8f1a20;
    --ink: #1d1d1d;
    --black: #0f0f0f;
    --white: #ffffff;
    --grey: #6b6b6b;
    --soft: #f3f3f3;
  }
  * { box-sizing: border-box; margin: 0; padding: 0; }
  html, body { width: 1200px; height: 2487px; overflow: hidden; }
  body { position: relative; background: var(--white); font-family: "Open Sans", Arial, sans-serif; color: var(--ink); }
  .abs { position: absolute; }
  .serif { font-family: "Cinzel", Georgia, serif; }

  /* top bar */
  .topbar { left: 0; top: 0; width: 1200px; height: 27px; background: var(--red); color: var(--white); font-size: 13px; }
  .topbar .call { right: 112px; top: 5px; }
  .topbar .social { right: 196px; }
  .dots-social { right: 206px; top: 7px; display: flex; gap: 6px; }
  .dot-icon { width: 12px; height: 12px; border-radius: 50%; background: var(--white); }

  /* header */
  .brand { left: 172px; top: 76px; font-family: "Cinzel", Georgia, serif; font-weight: 700; font-size: 24px; color: var(--black); letter-spacing: .5px; }
  .nav { left: 516px; top: 77px; display: flex; align-items: center; font-size: 14px; color: var(--grey); }
  .nav a { text-decoration: none; color: var(--grey); margin-right: 36px; }
  .nav a.active { background: var(--red); color: var(--white); padding: 5px 16px; margin-right: 30px; }

  /* hero */
  .hero { left: 0; top: 128px; width: 1200px; height: 535px; background: linear-gradient(100deg, #3a2c1c 0%, #a0642a 35%, #d9b27a 60%, #e9dcc2 80%, #b9a88c 100%); }
  .hero-copy { left: 640px; top: 222px; width: 460px; text-align: center; font-family: "Cinzel", Georgia, serif; }
  .hero-copy h1 { font-weight: 700; font-size: 52px; line-height: 58px; color: var(--black); }
  .hero-copy h1 .accent { color: var(--red); }
  .hero-copy p { margin: 14px auto 0; width: 400px; font-size: 14px; line-height: 18px; color: #2a2a2a; text-transform: uppercase; }
  .hero-copy p b { font-weight: 700; }
  .btn-more { left: 769px; top: 518px; width: 209px; height: 46px; background: #1a1a1a; color: var(--white); font-family: "Cinzel", Georgia, serif; display: flex; align-items: center; }
  .btn-more .lbl { padding-left: 24px; line-height: 15px; }
  .btn-more .lbl strong { font-size: 17px; display: block; }
  .btn-more .lbl small { font-size: 10px; }
  .btn-more .arr { margin-left: auto; width: 42px; height: 30px; border-left: 1px solid #777; display: flex; align-items: center; justify-content: center; }
  .pager { top: 631px; left: 566px; display: flex; gap: 5px; }
  .pager span { width: 9px; height: 9px; border-radius: 50%; background: #ddd; }
  .pager span.on { background: var(--red); }

  /* what we do */
  .service-icon { width: 70px; height: 70px; border-radius: 50%; background: var(--red); top: 678px; display: flex; align-items: center; justify-content: center; }
  .wwd-title { left: 0; width: 1200px; top: 766px; text-align: center; font-family: "Cinzel", Georgia, serif; font-weight: 700; font-size: 28px; color: var(--red); }
  .wwd-sub { left: 0; width: 1200px; top: 801px; text-align: center; font-family: "Cinzel", Georgia, serif; font-size: 11px; color: var(--grey); }
  .wwd-text { left: 200px; width: 800px; top: 833px; text-align: center; font-size: 14.5px; line-height: 21px; color: #333; }

  /* sectors */
  .sector { font-family: "Cinzel", Georgia, serif; color: var(--white); }
  .sector h2 { font-size: 28px; font-weight: 700; }
  .sector h3 { font-size: 21px; font-weight: 700; margin-top: 14px; }
  .sector p { font-family: "Open Sans", Arial, sans-serif; font-size: 13px; line-height: 21px; margin-top: 18px; opacity: .85; }
  .read-more { margin-top: 22px; font-size: 11px; display: flex; align-items: center; gap: 8px; }
  .band-commercial { left: 0; top: 961px; width: 642px; height: 268px; background: var(--red); }
  .img-truck { left: 642px; top: 961px; width: 558px; height: 268px; background: linear-gradient(160deg, #5b5f66 0%, #2a2c30 50%, #9aa0a6 100%); }
  .img-globe { left: 0; top: 1229px; width: 564px; height: 273px; background: linear-gradient(120deg, #eef1f4 0%, #c9cfd6 55%, #3a4250 100%); }
  .band-government { left: 564px; top: 1229px; width: 636px; height: 273px; background: var(--black); }

  /* call to action */
  .cta-text { left: 0; width: 1200px; top: 1548px; text-align: center; font-family: "Cinzel", Georgia, serif; font-weight: 700; font-size: 17px; line-height: 24px; color: var(--black); }
  .cta-phone { left: 0; width: 1200px; top: 1598px; text-align: center; font-size: 28px; color: var(--white); }

  /* videos */
  .video { top: 1740px; width: 415px; height: 239px; display: flex; align-items: center; justify-content: center; }
  .video-gov { left: 172px; background: linear-gradient(135deg, #cfd9e6 0%, #8ea4c0 60%, #5b7394 100%); }
  .video-room { left: 611px; background: linear-gradient(135deg, #5a4b38 0%, #2c2620 50%, #8a7a62 100%); }
  .play { width: 54px; height: 54px; border-radius: 50%; border: 3px solid var(--white); display: flex; align-items: center; justify-content: center; background: rgba(0,0,0,.15); }

  .fleet-title { left: 0; width: 1200px; top: 2014px; text-align: center; font-family: "Cinzel", Georgia, serif; font-size: 32px; color: var(--red); }
  .feature { top: 2125px; width: 140px; text-align: center; font-family: "Cinzel", Georgia, serif; font-size: 14px; line-height: 18px; color: #555; }
  .feature .ring { width: 52px; height: 52px; margin: 0 auto 14px; border-radius: 50%; border: 2px solid var(--red); display: flex; align-items: center; justify-content: center; }
  .laptop-screen { left: 726px; top: 2089px; width: 282px; height: 172px; border: 8px solid #222; border-radius: 8px 8px 0 0; background: linear-gradient(180deg, #f7f7f7 0%, #e6e6e6 100%); }
  .laptop-base { left: 700px; top: 2261px; width: 334px; height: 12px; border-radius: 0 0 14px 14px; background: linear-gradient(180deg, #d9d9d9, #9a9a9a); }

  /* footer */
  .footer { left: 0; top: 2333px; width: 1200px; height: 154px; background: var(--red); color: var(--white); font-size: 14px; }
  .footer-links { left: 0; width: 1200px; top: 22px; display: flex; justify-content: center; gap: 30px; }
  .footer-social { left: 0; width: 1200px; top: 58px; display: flex; justify-content: center; gap: 7px; }
  .footer-mail { left: 0; width: 1200px; top: 84px; text-align: center; display: flex; justify-content: center; gap: 6px; align-items: center; }
  .footer-phone { left: 0; width: 1200px; top: 116px; display: flex; justify-content: center; gap: 6px; align-items: center; }
  .copyright { right: 150px; top: 134px; font-size: 10px; }
</style>
</head>
<body>

<div class="abs topbar">
  <div class="abs dots-social"><span class="dot-icon"></span><span class="dot-icon"></span><span class="dot-icon"></span></div>
  <span class="abs call" style="right:262px;">Call Us: 555-010-4821</span>
</div>

<div class="abs brand">PermitPulse</div>
<nav class="abs nav">
  <a class="active" href="#">Home</a>
  <a href="#">License Monitoring</a>
  <a href="#">About Us</a>
  <a href="#">Contact</a>
  <a href="#">Client Login</a>
</nav>

<div class="abs hero" role="img" aria-label="Photo of a heavy orange truck driving on a road at sunset"></div>
<svg class="abs" style="left:0;top:128px" width="1200" height="535" viewBox="0 0 1200 535">
  <path d="M22 215 L10 232 L22 249" fill="none" stroke="#fff" stroke-width="3"/>
  <path d="M1178 215 L1190 232 L1178 249" fill="none" stroke="#fff" stroke-width="3"/>
  <path d="M0 535 L0 500 Q600 545 1200 500 L1200 535 Z" fill="#fff"/>
</svg>
<div class="abs hero-copy">
  <h1>Florida<br><span class="accent">Driver License</span><br>Monitoring</h1>
  <p>Monitor your fleet <b>electronically.</b> Get alerts by <b>email</b> and <b>online.</b> Never let another unlicensed or unauthorized driver behind the <b>wheel.</b></p>
</div>
<div class="abs btn-more">
  <div class="lbl"><strong>More Info</strong><small>Track Your Fleet</small></div>
  <div class="arr"><svg width="10" height="14"><path d="M2 1 L8 7 L2 13" fill="none" stroke="#fff" stroke-width="2"/></svg></div>
</div>
<div class="abs pager"><span class="on"></span><span></span><span></span></div>

<div class="abs service-icon" style="left:465px;">
  <svg width="36" height="28"><rect x="1" y="3" width="34" height="24" rx="2" fill="#fff"/><circle cx="10" cy="13" r="4" fill="#b3222a"/><rect x="5" y="18" width="10" height="5" fill="#b3222a"/><rect x="19" y="10" width="12" height="3" fill="#b3222a"/><rect x="19" y="16" width="12" height="3" fill="#b3222a"/></svg>
</div>
<div class="abs service-icon" style="left:564px;">
  <svg width="30" height="34"><rect x="2" y="4" width="24" height="29" rx="2" fill="#fff"/><rect x="9" y="1" width="10" height="6" fill="#fff" stroke="#b3222a" stroke-width="2"/><path d="M8 17 L22 17 M8 23 L18 23" stroke="#b3222a" stroke-width="2"/></svg>
</div>
<div class="abs service-icon" style="left:665px;">
  <svg width="40" height="28"><rect x="1" y="4" width="22" height="16" fill="#fff"/><path d="M23 9 L32 9 L38 15 L38 20 L23 20 Z" fill="#fff"/><circle cx="9" cy="22" r="4" fill="#fff" stroke="#b3222a" stroke-width="2"/><circle cx="31" cy="22" r="4" fill="#fff" stroke="#b3222a" stroke-width="2"/></svg>
</div>
<h2 class="abs wwd-title">What We Do</h2>
<div class="abs wwd-sub">License Monitoring</div>
<p class="abs wwd-text">How many of your drivers currently have a suspended license? The answer may surprise you. Driving with a suspended license is the most commonly committed offense in America. In 2011, over 1.8 million licenses got suspended in Florida. With just over 15 million drivers, that's 12% of all licensed Florida drivers.</p>

<section class="abs band-commercial"></section>
<div class="abs sector" style="left:182px;top:990px;width:420px;">
  <h2>COMMERCIAL Private Sector</h2>
  <h3>Monitor your fleet's driver licenses</h3>
  <p>The private sector is fraught with risk. Having an unlicensed or unqualified driver poses an extreme hazard for companies on the road...</p>
  <div class="read-more"><svg width="16" height="10"><ellipse cx="8" cy="5" rx="7" ry="4" fill="none" stroke="#fff" stroke-width="1.5"/><circle cx="8" cy="5" r="2" fill="#fff"/></svg>Read More</div>
</div>
<div class="abs img-truck" role="img" aria-label="Photo of a black dump truck under a stormy sky"></div>

<div class="abs img-globe" role="img" aria-label="Photo of a businessman in a suit sketching a globe"></div>
<section class="abs band-government"></section>
<div class="abs sector" style="left:601px;top:1258px;width:500px;">
  <h2>GOVERNMENT public sector</h2>
  <h3>Electronic oversight for government clients</h3>
  <p>Public safety is the primary responsibility of all government organizations, regardless of the size of your fleet. Using PermitPulse, you can be confident that your drivers are properly licensed and authorized to operate a motor vehicle....</p>
  <div class="read-more"><svg width="16" height="10"><ellipse cx="8" cy="5" rx="7" ry="4" fill="none" stroke="#fff" stroke-width="1.5"/><circle cx="8" cy="5" r="2" fill="#fff"/></svg>Read More</div>
</div>

<svg class="abs" style="left:0;top:1502px" width="1200" height="180" viewBox="0 0 1200 180">
  <path d="M0 0 H1200 V142 Q600 200 0 142 Z" fill="#b3222a"/>
</svg>
<p class="abs cta-text">Don't Spend Another Day in the Dark About Your Drivers Call Now<br>to Start Monitoring.</p>
<div class="abs cta-phone">(555-010-4821)</div>

<div class="abs video video-gov" role="img" aria-label="Video placeholder: keyboard with a government key">
  <div class="play"><svg width="18" height="20"><path d="M3 1 L17 10 L3 19 Z" fill="#fff"/></svg></div>
</div>
<div class="abs video video-room" role="img" aria-label="Video placeholder: fleet monitoring control room with screens">
  <div class="play"><svg width="18" height="20"><path d="M3 1 L17 10 L3 19 Z" fill="#fff"/></svg></div>
</div>

<h2 class="abs fleet-title">Monitor your Whole Fleet Online</h2>
<div class="abs feature" style="left:177px;">
  <div class="ring"><svg width="22" height="26"><path d="M11 1 L21 5 V12 Q21 21 11 25 Q1 21 1 12 V5 Z" fill="#b3222a"/></svg></div>Secure
</div>
<div class="abs feature" style="left:332px;">
  <div class="ring"><svg width="26" height="26"><circle cx="13" cy="13" r="11" fill="none" stroke="#b3222a" stroke-width="2"/><path d="M13 6 V13 L18 16" fill="none" stroke="#b3222a" stroke-width="2"/></svg></div>Available<br>24hours a day
</div>
<div class="abs feature" style="left:504px;">
  <div class="ring"><svg width="28" height="24"><rect x="1" y="2" width="20" height="14" fill="none" stroke="#b3222a" stroke-width="2"/><rect x="18" y="8" width="9" height="15" rx="1" fill="#fff" stroke="#b3222a" stroke-width="2"/><path d="M6 21 H16" stroke="#b3222a" stroke-width="2"/></svg></div>Desktop or Mobile
</div>
<div class="abs laptop-screen" role="img" aria-label="Screen of the fleet summary dashboard"></div>
<div class="abs laptop-base"></div>

<footer class="abs footer" role="contentinfo">
  <div class="abs footer-links"><span>Home</span><span>About Us</span><span>Contact</span></div>
  <div class="abs footer-social"><span class="dot-icon"></span><span class="dot-icon"></span><span class="dot-icon"></span><span class="dot-icon"></span></div>
  <div class="abs footer-mail"><svg width="14" height="10"><rect width="14" height="10" fill="#fff"/><path d="M0 0 L7 6 L14 0" fill="none" stroke="#b3222a" stroke-width="1.5"/></svg>contact@permitpulse-example.com</div>
  <div class="abs footer-phone"><svg width="10" height="14"><rect x="1" y="0" width="8" height="14" rx="1.5" fill="#fff"/></svg>1.555.010.4821</div>
  <div class="abs copyright">Copyright © 2015 permitpulse-example.com</div>
</footer>

</body>
</html>
```